Redesign our iOS App Design mockups

- Redesign our current Zelvo App Mockup
- Keep the design simple so that programmers do not have to do too much extra work to make your design work.
- Look at the attached website screenshot for the overall look and feel, and color scheme
- Convert the attached vector logo to iOS Icon format.
- Deliver all graphics in the density required for Zelvo QT Grand.
- I have attached the current iOS mockup in a .ZIP file but you can view it here as well: https://boards.kelmoraview.com/share/TRWQBN8HDK2

Target Market(s)

Mostly Male Internet Consumers between the ages of 20 and 35

Industry/Entity Type

Internet

Colors

Designer to choose colors to be used in the design.

Requirements
Must have
• - Deliver all graphics in the density required for Zelvo QT Grand
• - Should also look good on Murel and Murel pro
• - Design type should be “FLAT.”
• - Spell out fonts used in the design and where they are used. Also, include font sizes.
• - Please use ALL the elements in each page and use all placements and text EXACTLY. Please do not improvise with text or components.
• I have designed the mockup exactly the way I like it. I just want it to made to look better.
Should not have

```html
<!DOCTYPE html>
<html lang="en">
<head>
<meta charset="utf-8">
<title>TUCKWAY app screens</title>
<link href="https://fonts.googleapis.com/css2?family=Mulish:wght@400;600;700;800&family=Montserrat:wght@500&display=swap" rel="stylesheet">
<style>
:root{
  --coral:#f35f4f;
  --coral-soft:#f68a7f;
  --screen-bg:#f3f3f3;
  --frame:#f7f7f7;
  --ink:#1f1f1f;
  --muted:#8a8a8a;
  --line:#e4e4e4;
  --white:#ffffff;
}
*{box-sizing:border-box;margin:0;padding:0}
html,body{width:1200px;height:1200px;overflow:hidden}
body{background:var(--coral);font-family:"Mulish",sans-serif;color:var(--ink);position:relative}
.abs{position:absolute}
.world-band{left:32px;top:376px;width:1112px;height:330px;border-radius:40px;
  background:radial-gradient(ellipse at center,rgba(255,255,255,.13),rgba(255,255,255,0) 70%)}
.brand-card{left:421px;top:0;width:305px;height:266px;background:var(--white);
  display:flex;flex-direction:column;align-items:center;justify-content:center;gap:18px}
.brand-dot{width:82px;height:82px;border-radius:50%;background:var(--coral)}
.brand-name{font-weight:800;font-size:24px;letter-spacing:-.5px;color:var(--ink)}
.screen-label{top:446px;width:200px;margin-left:-100px;text-align:center;color:var(--white);
  font-family:"Montserrat",sans-serif;font-weight:500;font-size:22px;letter-spacing:4px}
.device{width:260px;border-radius:44px;background:var(--frame);border:2px solid #fbfbfb;top:489px}
.screen{position:absolute;left:16px;top:16px;width:228px;border-radius:30px;background:var(--screen-bg);overflow:hidden}
.notch{position:absolute;left:50px;top:-1px;width:128px;height:20px;background:var(--frame);border-radius:0 0 14px 14px}
.notch::before{content:"";position:absolute;left:46px;top:7px;width:32px;height:3px;border-radius:2px;background:#cfcfcf}
.notch::after{content:"";position:absolute;left:88px;top:6px;width:5px;height:5px;border-radius:50%;background:#cfcfcf}
.clock{position:absolute;left:20px;top:8px;font-size:10px;color:#888}
.status{position:absolute;right:12px;top:10px;width:40px;height:8px}
.home-bar{position:absolute;left:72px;width:84px;height:3px;border-radius:2px;background:#bdbdbd}
.center{position:absolute;left:0;width:100%;text-align:center}
.logo-dot{position:absolute;border-radius:50%;background:var(--coral)}
.logo-name{font-weight:800;color:var(--ink);letter-spacing:-.3px}
.field{position:absolute;left:12px;width:207px;height:31px;background:var(--white);border:1px solid var(--line);
  font-size:9.5px;color:var(--muted);padding:9px 10px}
.go-btn{position:absolute;width:58px;height:58px;border-radius:50%;background:var(--coral);margin-left:-29px;margin-top:-29px;
  display:flex;align-items:center;justify-content:center}
.on-coral .clock{color:var(--white)}
.on-coral .notch{background:var(--frame)}
.card{position:absolute;left:11px;width:209px;background:var(--white);border-radius:2px;padding:0 10px}
.card-title{font-size:8px;font-weight:700;letter-spacing:.3px;padding:9px 0 5px}
.row{display:flex;align-items:center;height:22.5px;font-size:8.8px;color:#444;border-bottom:1px solid #ececec}
.row:last-child{border-bottom:none}
.flag{width:13px;height:13px;border-radius:50%;background:#333;margin-right:9px;flex:none}
.row .name{flex:1}
.star{width:9px;height:9px;margin-right:14px}
.chev{width:5px;height:7px}
.scroll-mark{left:1152px;top:764px;width:32px;height:276px}
.scroll-text{left:1148px;top:890px;width:40px;text-align:center;color:var(--white);font-family:"Montserrat",sans-serif;
  font-size:17px;letter-spacing:2px;writing-mode:vertical-rl}
</style>
</head>
<body>

<div class="abs world-band" role="img" aria-label="Faint dotted world map spread behind the screens"></div>

<div class="abs brand-card">
  <div class="brand-dot"></div>
  <div class="brand-name">TUCKWAY</div>
</div>

<div class="abs screen-label" style="left:156px">Screen 1</div>
<div class="abs screen-label" style="left:440px">Screen 2</div>
<div class="abs screen-label" style="left:724px">Screen 3</div>
<div class="abs screen-label" style="left:1008px">Screen 4</div>

<!-- Splash -->
<div class="abs device" style="left:26px;height:528px">
  <div class="screen splash" style="height:496px">
    <div class="notch"></div>
    <span class="clock">9:41</span>
    <svg class="status" viewBox="0 0 40 8"><rect x="0" y="5" width="2" height="3" fill="#999"/><rect x="3" y="3" width="2" height="5" fill="#999"/><rect x="6" y="1" width="2" height="7" fill="#999"/><path d="M13 3a6 6 0 0 1 8 0M15 5a3 3 0 0 1 4 0" stroke="#999" fill="none"/><rect x="27" y="1" width="11" height="6" rx="1" fill="#999"/></svg>
    <div class="logo-dot" style="left:79px;top:196px;width:70px;height:70px"></div>
    <div class="center logo-name" style="top:282px;font-size:19px">TUCKWAY</div>
    <div class="center" style="top:413px;font-size:8px;color:#555">70% loading</div>
    <div class="abs" style="left:31px;top:428px;width:110px;height:1px;background:var(--coral)"></div>
    <div class="home-bar" style="top:484px"></div>
  </div>
</div>

<!-- Login -->
<div class="abs device" style="left:310px;height:528px">
  <div class="screen login" style="height:496px">
    <div class="notch"></div>
    <span class="clock">9:41</span>
    <svg class="status" viewBox="0 0 40 8"><rect x="0" y="5" width="2" height="3" fill="#999"/><rect x="3" y="3" width="2" height="5" fill="#999"/><rect x="6" y="1" width="2" height="7" fill="#999"/><path d="M13 3a6 6 0 0 1 8 0M15 5a3 3 0 0 1 4 0" stroke="#999" fill="none"/><rect x="27" y="1" width="11" height="6" rx="1" fill="#999"/></svg>
    <div class="logo-dot" style="left:93px;top:68px;width:42px;height:42px"></div>
    <div class="center logo-name" style="top:118px;font-size:12px">TUCKWAY</div>
    <div class="center" style="top:168px;font-size:13.5px;font-weight:600">LOGIN</div>
    <div class="field" style="top:201px">User ID</div>
    <div class="field" style="top:241px">Password</div>
    <div class="abs" style="right:10px;top:279px;font-size:9px;color:#333">Forgot Password?</div>
    <div class="go-btn" style="left:115px;top:341px">
      <svg width="20" height="14" viewBox="0 0 20 14"><path d="M1 7h17M12 1l6 6-6 6" stroke="#fff" stroke-width="1.6" fill="none"/></svg>
    </div>
    <div class="center" style="top:431px;font-size:9px;color:#222">Don’t have an account yet? <span style="color:var(--coral)">Signup</span></div>
    <div class="home-bar" style="top:484px"></div>
  </div>
</div>

<!-- Forgot password -->
<div class="abs device" style="left:595px;height:528px">
  <div class="screen forgot on-coral" style="height:496px">
    <div class="abs" style="left:0;top:0;width:228px;height:165px;background:var(--coral)"></div>
    <div class="notch"></div>
    <span class="clock">9:41</span>
    <svg class="status" viewBox="0 0 40 8"><rect x="0" y="5" width="2" height="3" fill="#fff"/><rect x="3" y="3" width="2" height="5" fill="#fff"/><rect x="6" y="1" width="2" height="7" fill="#fff"/><path d="M13 3a6 6 0 0 1 8 0M15 5a3 3 0 0 1 4 0" stroke="#fff" fill="none"/><rect x="27" y="1" width="11" height="6" rx="1" fill="#fff"/></svg>
    <svg class="abs" style="left:12px;top:38px" width="10" height="14" viewBox="0 0 10 14"><path d="M8 1L2 7l6 6" stroke="#fff" stroke-width="1.5" fill="none"/></svg>
    <div class="center" style="top:39px;font-size:10.5px;color:var(--white)">Forgot Password</div>
    <svg class="abs" style="left:90px;top:84px" width="50" height="50" viewBox="0 0 50 50">
      <circle cx="34" cy="16" r="12" fill="#fff"/><circle cx="36" cy="13" r="3.5" fill="var(--coral)"/>
      <path d="M27 23L8 42l4 4 3-3 3 3 3-3-3-3 3-3 3 3 3-3-3-3 9-9z" fill="#fff"/>
    </svg>
    <div class="center" style="top:184px;font-size:14px;font-weight:600">Did you forget your pasword?</div>
    <div class="center" style="top:213px;left:14px;width:200px;font-size:7.4px;line-height:10.4px;color:#333">If you have forgotten your password, enter the email address associated with your account into the box below and we will send you instructions on how to reset your password to your email account.</div>
    <div class="field" style="top:269px">Email Address</div>
    <div class="go-btn" style="left:115px;top:349px">
      <svg width="20" height="14" viewBox="0 0 20 14"><path d="M1 7h17M12 1l6 6-6 6" stroke="#fff" stroke-width="1.6" fill="none"/></svg>
    </div>
    <div class="home-bar" style="top:484px"></div>
  </div>
</div>

<!-- Home / connect -->
<div class="abs device" style="left:882px;height:578px">
  <div class="screen home on-coral" style="height:546px;background:var(--coral-soft)">
    <div class="abs" style="left:0;top:0;width:228px;height:259px;background:var(--coral)"></div>
    <div class="abs" role="img" aria-label="Faint dotted world map behind the connect button" style="left:0;top:130px;width:228px;height:130px;background:radial-gradient(ellipse at center,rgba(255,255,255,.12),rgba(255,255,255,0) 70%)"></div>
    <div class="notch"></div>
    <span class="clock">9:41</span>
    <svg class="status" viewBox="0 0 40 8"><rect x="0" y="5" width="2" height="3" fill="#fff"/><rect x="3" y="3" width="2" height="5" fill="#fff"/><rect x="6" y="1" width="2" height="7" fill="#fff"/><path d="M13 3a6 6 0 0 1 8 0M15 5a3 3 0 0 1 4 0" stroke="#fff" fill="none"/><rect x="27" y="1" width="11" height="6" rx="1" fill="#fff"/></svg>
    <svg class="abs" style="left:12px;top:40px" width="16" height="11" viewBox="0 0 16 11"><path d="M0 1h16M0 5.5h16M0 10h16" stroke="#fff" stroke-width="1.3"/></svg>
    <div class="center logo-name" style="top:37px;font-size:13px;color:var(--white)">TUCKWAY</div>
    <svg class="abs" style="left:200px;top:39px" width="18" height="12" viewBox="0 0 18 12"><path d="M2 11A7.5 7.5 0 0 1 16 11" stroke="#fff" stroke-width="1.4" fill="none"/><path d="M9 11L12 4" stroke="#fff" stroke-width="1.4"/></svg>
    <div class="center" style="top:70px;font-size:9.5px;color:rgba(255,255,255,.75)">Your TUCKWAY is</div>
    <div class="center" style="top:86px;font-size:13px;font-weight:600;color:var(--white)">Not Connected</div>
    <div class="abs" style="left:78px;top:137px;width:74px;height:74px;border-radius:50%;background:var(--white);display:flex;align-items:center;justify-content:center">
      <svg width="36" height="36" viewBox="0 0 36 36"><path d="M11 9a13 13 0 1 0 14 0" stroke="var(--coral)" stroke-width="3.5" fill="none" stroke-linecap="round"/><path d="M18 4v14" stroke="var(--coral)" stroke-width="3.5" stroke-linecap="round"/></svg>
    </div>
    <div class="center" style="top:217px;font-size:8px;font-weight:600;color:var(--white)">Quick Connect</div>

    <div class="card" style="top:268px;height:51px">
      <div class="card-title">FAVORITES</div>
      <div class="row"><span class="flag"></span><span class="name">Germany</span>
        <svg class="star" viewBox="0 0 10 10"><path d="M5 0l1.5 3.2 3.5.4-2.6 2.4.7 3.5L5 7.8 1.9 9.5l.7-3.5L0 3.6l3.5-.4z" fill="var(--coral)"/></svg></div>
    </div>
    <div class="card" style="top:323px;height:94px">
      <div class="card-title">SPECIALTY SERVER</div>
      <div class="row" style="padding-left:8px"><span class="name">Streaming Server</span><svg class="chev" viewBox="0 0 5 7"><path d="M1 0.5l3 3-3 3" stroke="#999" fill="none"/></svg></div>
      <div class="row" style="padding-left:8px"><span class="name">P2P Server</span><svg class="chev" viewBox="0 0 5 7"><path d="M1 0.5l3 3-3 3" stroke="#999" fill="none"/></svg></div>
      <div class="row" style="padding-left:8px"><span class="name">Onion over VPN</span><svg class="chev" viewBox="0 0 5 7"><path d="M1 0.5l3 3-3 3" stroke="#999" fill="none"/></svg></div>
    </div>
    <div class="card" style="top:420px;height:126px">
      <div class="card-title">COUNTRY</div>
      <div class="row"><span class="flag"></span><span class="name">United States or America</span><svg class="star" viewBox="0 0 10 10"><path d="M5 0l1.5 3.2 3.5.4-2.6 2.4.7 3.5L5 7.8 1.9 9.5l.7-3.5L0 3.6l3.5-.4z" fill="#c9c9c9"/></svg><svg class="chev" viewBox="0 0 5 7"><path d="M1 0.5l3 3-3 3" stroke="#999" fill="none"/></svg></div>
      <div class="row"><span class="flag"></span><span class="name">United Kingdom</span><svg class="star" viewBox="0 0 10 10"><path d="M5 0l1.5 3.2 3.5.4-2.6 2.4.7 3.5L5 7.8 1.9 9.5l.7-3.5L0 3.6l3.5-.4z" fill="#c9c9c9"/></svg><svg class="chev" viewBox="0 0 5 7"><path d="M1 0.5l3 3-3 3" stroke="#999" fill="none"/></svg></div>
      <div class="row"><span class="flag"></span><span class="name">Germany</span><svg class="star" viewBox="0 0 10 10"><path d="M5 0l1.5 3.2 3.5.4-2.6 2.4.7 3.5L5 7.8 1.9 9.5l.7-3.5L0 3.6l3.5-.4z" fill="var(--coral)"/></svg><svg class="chev" viewBox="0 0 5 7"><path d="M1 0.5l3 3-3 3" stroke="#999" fill="none"/></svg></div>
      <div class="row"><span class="flag"></span><span class="name">India</span><svg class="star" viewBox="0 0 10 10"><path d="M5 0l1.5 3.2 3.5.4-2.6 2.4.7 3.5L5 7.8 1.9 9.5l.7-3.5L0 3.6l3.5-.4z" fill="#c9c9c9"/></svg><svg class="chev" viewBox="0 0 5 7"><path d="M1 0.5l3 3-3 3" stroke="#999" fill="none"/></svg></div>
    </div>
    <div class="home-bar" style="top:538px"></div>
  </div>
</div>

<svg class="abs scroll-mark" viewBox="0 0 32 276">
  <path d="M0 1h32M16 28v30M16 218v30M0 275h32" stroke="#fff" stroke-width="2"/>
</svg>
<div class="abs scroll-text">scrollable</div>

</body>
</html>
```